Photography Business, Business Card

Looking for a unique cutting edge card that takes advantage of the latest printing technologies. Please review this site for all the options they office: https://plumeprints.example. If you can think it they can do it. And if you have an idea and do not know if they can do it, I will check into it.
Updates

Target Market(s)

People and places I took images of and future clients.

Industry/Entity Type

Photography

Contact Information for Business Card

Name, cell & email. Colin Hartley, chartley@kvnphoto.example, 318-742-9061

Colors

Designer to choose only greyscale colors for use in the design.

Requirements
Must have
• 100% cutting edge. Is so great, those I hand it to always show it to someone else. A piece of art.
Nice to have
• Blacks, silvers, greys, some red. Maybe other colors?

```html
<!DOCTYPE html>
<html lang="en">
<head>
<meta charset="utf-8">
<title>KVN Multimedia – Folding Camera Business Card</title>
<link rel="stylesheet" href="https://fonts.googleapis.com/css2?family=Mrs+Saint+Delafield&family=Noto+Serif:wght@700&family=Poppins:wght@400&family=Open+Sans:wght@400&display=swap">
<style>
  :root {
    --stage-grey: #a9a8a7;
    --card-black: #000000;
    --card-white: #ffffff;
    --accent-red: #ff0016;
    --blade-grey: #4a4a4a;
    --label-ink: #111111;
  }
  html, body {
    margin: 0;
    padding: 0;
    width: 1200px;
    height: 853px;
    overflow: hidden;
    background: var(--stage-grey);
  }
  .sheet { display: block; width: 1200px; height: 853px; }
  .brand-word { font-family: "Noto Serif", serif; font-weight: 700; }
  .brand-word--white { fill: var(--card-white); }
  .brand-word--red { fill: var(--accent-red); }
  .signature-name { font-family: "Mrs Saint Delafield", cursive; fill: var(--accent-red); }
  .contact-line { font-family: "Poppins", sans-serif; font-weight: 400; fill: var(--card-black); }
  .print-note { font-family: "Open Sans", sans-serif; font-size: 22px; fill: var(--label-ink); }
  .fold-line { stroke: var(--label-ink); stroke-width: 3; stroke-dasharray: 7 5; fill: none; }
</style>
</head>
<body>
<svg class="sheet" viewBox="0 0 2284 1615" preserveAspectRatio="none" xmlns="http://www.w3.org/2000/svg">
  <defs>
    <clipPath id="front-left-half"><rect x="0" y="0" width="652" height="1615"/></clipPath>
    <clipPath id="front-right-half"><rect x="652" y="0" width="1632" height="1615"/></clipPath>
    <clipPath id="back-body">
      <path d="M1264 213 L1286 181 L1407 181 L1430 213 L2030 213 Q2105 213 2105 288 L2105 661 Q2105 736 2030 736 L1264 736 Q1189 736 1189 661 L1189 288 Q1189 213 1264 213 Z"/>
    </clipPath>
    <clipPath id="inner-white-flap">
      <path d="M188 805 L1062 805 L1062 1168 L1115 1205 L1115 1410 L1062 1447 L1062 1443 Q1062 1568 937 1568 L313 1568 Q188 1568 188 1443 Z"/>
    </clipPath>
    <clipPath id="inner-black-flap">
      <path d="M1211 804 L2084 804 L2084 1442 Q2084 1567 1959 1567 L1336 1567 Q1211 1567 1211 1442 Z"/>
    </clipPath>
    <radialGradient id="aperture-tone" cx="50%" cy="50%" r="50%">
      <stop offset="0%" stop-color="#5a5a5a"/>
      <stop offset="100%" stop-color="#3e3e3e"/>
    </radialGradient>
  </defs>

  <!-- Front outer face -->
  <g class="card card--front">
    <path class="front-black-half" fill="var(--card-black)" d="M268 197 L652 197 L652 720 L268 720 Q193 720 193 645 L193 272 Q193 197 268 197 Z"/>
    <path class="front-white-half" fill="var(--card-white)" d="M652 197 L870 197 L891 165 L1013 165 L1035 197 Q1108 197 1108 270 L1108 645 Q1108 720 1033 720 L652 720 Z"/>
    <g class="lens-ring">
      <circle cx="652" cy="450" r="196" fill="var(--accent-red)" clip-path="url(#front-right-half)"/>
      <circle cx="652" cy="450" r="160" fill="var(--card-black)" clip-path="url(#front-right-half)"/>
      <circle cx="652" cy="450" r="160" fill="var(--accent-red)" clip-path="url(#front-left-half)"/>
      <circle cx="652" cy="450" r="125" fill="var(--stage-grey)"/>
    </g>
    <text class="brand-word brand-word--red" font-size="60" text-anchor="middle" transform="translate(338 447) rotate(-90)">KVN</text>
    <text class="brand-word brand-word--white" font-size="50" text-anchor="middle" transform="translate(423 455) rotate(-90)" textLength="330" lengthAdjust="spacingAndGlyphs">MULTIMEDIA</text>
    <text class="signature-name" font-size="120" text-anchor="middle" transform="translate(905 450) rotate(-90)">Colin Hartley</text>
    <text class="contact-line" font-size="32" transform="translate(992 632) rotate(-90)">chartley@kvnphoto.example</text>
    <text class="contact-line" font-size="32" transform="translate(1025 632) rotate(-90)">318-742-9061</text>
    <line class="fold-line" x1="652" y1="145" x2="652" y2="758"/>
    <text class="print-note" transform="translate(657 145) rotate(-90)">fold area</text>
  </g>

  <!-- Back face -->
  <g class="card card--back">
    <path fill="var(--card-black)" d="M1264 213 L1286 181 L1407 181 L1430 213 L2030 213 Q2105 213 2105 288 L2105 661 Q2105 736 2030 736 L1264 736 Q1189 736 1189 661 L1189 288 Q1189 213 1264 213 Z"/>
    <g clip-path="url(#back-body)">
      <circle cx="1647" cy="467" r="315" fill="url(#aperture-tone)" role="img" aria-label="Camera shutter aperture blades in dark grey with one deep red blade"/>
      <circle cx="1647" cy="467" r="125" fill="var(--stage-grey)"/>
    </g>
    <text class="print-note" x="1662" y="190" text-anchor="middle">Bottom</text>
  </g>

  <!-- Inner white flap -->
  <g class="card card--inner-white">
    <path fill="var(--card-white)" d="M188 805 L1062 805 L1062 1168 L1115 1205 L1115 1410 L1062 1447 L1062 1443 Q1062 1568 937 1568 L313 1568 Q188 1568 188 1443 Z"/>
    <g clip-path="url(#inner-white-flap)">
      <circle cx="638" cy="805" r="328" fill="var(--accent-red)"/>
      <circle cx="638" cy="805" r="270" fill="var(--card-black)"/>
      <circle cx="638" cy="805" r="212" fill="var(--stage-grey)"/>
    </g>
    <text class="signature-name" x="640" y="1235" font-size="150" text-anchor="middle">Colin Hartley</text>
    <text class="contact-line" x="333" y="1375" font-size="48">chartley@kvnphoto.example</text>
    <text class="contact-line" x="333" y="1428" font-size="48">318-742-9061</text>
    <text class="print-note" transform="translate(168 1118) rotate(-90)">Part of fold</text>
  </g>

  <!-- Inner black flap -->
  <g class="card card--inner-black">
    <path fill="var(--card-black)" d="M1211 804 L2084 804 L2084 1442 Q2084 1567 1959 1567 L1336 1567 Q1211 1567 1211 1442 Z"/>
    <g clip-path="url(#inner-black-flap)">
      <circle cx="1634" cy="804" r="270" fill="var(--accent-red)"/>
      <circle cx="1634" cy="804" r="212" fill="var(--stage-grey)"/>
    </g>
    <text class="brand-word brand-word--white" font-size="92" text-anchor="middle" textLength="550" lengthAdjust="spacingAndGlyphs" transform="translate(1640 1212) rotate(180)">MULTIMEDIA</text>
    <text class="brand-word brand-word--red" font-size="110" text-anchor="middle" transform="translate(1647 1335) rotate(180)">KVN</text>
    <text class="print-note" transform="translate(1190 1073) rotate(-90)">Part of fold</text>
  </g>
</svg>
</body>
</html>
```